Orchard Beds: A Simple Handbook for Newcomers

I need a book cover design for a book showing a Permaculture Garden. The sub title is : Zero Skills Required, Easy-Care Methods To Grow A Greener, Planet-Kind Plot That Flourishes Right On Tiny Balconies

Down to earth colors but with something bright to catch the eye

First time using this so my apologies. I believe I posted the colors which are good. I mentioned it is for Permaculture Gardening which is a lot different from just regular till and plant gardens. They tend to try not to dig too much, plant with other plants that help each other and let the dead stuff just rot into the ground so they automatically feed the soil around it.
I don’t want a white background ( someone else used, that is why I mention). Realistic (ish) Gardening type tools (no shovel 😀) like maybe a watering can or a marker for a type of plant, etc. I do want a brighter color somehow within to help catch the eye.

```html
<!DOCTYPE html>
<html lang="en">
<head>
<meta charset="utf-8">
<title>Orchard Beds: A Simple Handbook for Newcomers</title>
<link href="https://fonts.googleapis.com/css2?family=Oswald:wght@400;500;600;700&display=swap" rel="stylesheet">
<style>
  :root {
    --page: #ffffff;
    --leaf-green: #1b8140;
    --deep-green: #17703a;
    --bright-yellow: #f2eb2b;
    --paper-white: #ffffff;
    --photo-dark: #2f4a2a;
    --photo-mid: #5f8a3e;
    --photo-light: #9bb879;
    --path-tan: #b9ad94;
  }
  html, body {
    margin: 0;
    padding: 0;
    width: 1200px;
    height: 1200px;
    overflow: hidden;
    background: var(--page);
  }
  .canvas {
    position: relative;
    width: 1200px;
    height: 1200px;
    background: var(--page);
  }
  .book-cover {
    position: absolute;
    left: 254px;
    top: 82px;
    width: 692px;
    height: 1036px;
    background: var(--leaf-green);
    overflow: hidden;
    font-family: "Oswald", "Arial Narrow", sans-serif;
    text-align: center;
  }
  .title {
    position: absolute;
    left: 0;
    right: 0;
    top: 26px;
    margin: 0;
    text-transform: uppercase;
    line-height: 1;
  }
  .title-line-one {
    display: block;
    color: var(--bright-yellow);
    font-weight: 600;
    font-size: 118px;
    letter-spacing: 1px;
  }
  .title-line-two {
    display: block;
    margin-top: 0;
    color: var(--paper-white);
    font-weight: 400;
    font-size: 152px;
    letter-spacing: 2px;
  }
  .tagline-pill {
    position: absolute;
    left: 46px;
    top: 321px;
    width: 602px;
    height: 62px;
    border-radius: 31px;
    background: var(--bright-yellow);
    color: var(--deep-green);
    font-weight: 500;
    font-size: 38px;
    line-height: 62px;
    text-transform: uppercase;
    white-space: nowrap;
  }
  .subtitle {
    position: absolute;
    left: 30px;
    right: 30px;
    top: 412px;
    margin: 0;
    color: var(--paper-white);
    font-weight: 400;
    font-size: 29px;
    line-height: 49px;
    text-transform: uppercase;
  }
  .garden-photo {
    position: absolute;
    left: 0;
    top: 600px;
    width: 692px;
    height: 375px;
    background:
      radial-gradient(ellipse at 30% 75%, var(--photo-mid) 0%, transparent 55%),
      radial-gradient(ellipse at 75% 60%, var(--photo-light) 0%, transparent 50%),
      linear-gradient(180deg, var(--path-tan) 0%, var(--photo-mid) 35%, var(--photo-dark) 100%);
  }
  .torn-edge {
    position: absolute;
    left: 0;
    top: 570px;
    width: 692px;
    height: 80px;
    display: block;
  }
  .author-band {
    position: absolute;
    left: 0;
    bottom: 0;
    width: 692px;
    height: 61px;
    background: var(--bright-yellow);
    color: var(--deep-green);
    font-weight: 700;
    font-size: 40px;
    line-height: 61px;
    letter-spacing: 4px;
    text-transform: uppercase;
  }
</style>
</head>
<body>
  <main class="canvas">
    <section class="book-cover">
      <h1 class="title">
        <span class="title-line-one">Orchard</span>
        <span class="title-line-two">Beds</span>
      </h1>
      <div class="tagline-pill">A Simple Handbook for Newcomers</div>
      <p class="subtitle">
        Zero Skills Required, Easy-Care Methods<br>
        To Grow A Greener, Planet-Kind Plot<br>
        That Flourishes Right On Tiny Balconies
      </p>
      <div class="garden-photo" role="img" aria-label="Aerial view of a community permaculture garden with raised vegetable beds, paths, a small shed and surrounding trees"></div>
      <svg class="torn-edge" viewBox="0 0 692 80" preserveAspectRatio="none" aria-hidden="true">
        <path fill="var(--leaf-green)" d="M0 0 H692 V62 L680 58 L668 64 L652 56 L640 60 L626 52 L612 55 L598 50 L585 54 L570 46 L556 50 L540 44 L526 48 L512 40 L498 43 L484 36 L470 32 L458 38 L446 30 L432 34 L418 40 L404 44 L392 50 L378 47 L364 52 L350 48 L336 54 L322 51 L308 56 L294 52 L280 57 L266 53 L252 58 L238 55 L224 60 L210 56 L196 61 L182 57 L168 62 L154 58 L140 63 L126 60 L112 64 L98 60 L84 65 L70 62 L56 66 L42 63 L28 67 L14 64 L0 68 Z"/>
        <path fill="none" stroke="var(--paper-white)" stroke-width="5" d="M0 68 L14 64 L28 67 L42 63 L56 66 L70 62 L84 65 L98 60 L112 64 L126 60 L140 63 L154 58 L168 62 L182 57 L196 61 L210 56 L224 60 L238 55 L252 58 L266 53 L280 57 L294 52 L308 56 L322 51 L336 54 L350 48 L364 52 L378 47 L392 50 L404 44 L418 40 L432 34 L446 30 L458 38 L470 32 L484 36 L498 43 L512 40 L526 48 L540 44 L556 50 L570 46 L585 54 L598 50 L612 55 L626 52 L640 60 L652 56 L668 64 L680 58 L692 62"/>
      </svg>
      <div class="author-band">Author Name</div>
    </section>
  </main>
</body>
</html>
```